" Possui corretores credenciados que vendem lotes e terrenos no Vale do Paraíba. A empresa não possui escritório próprio, os corretores trabalham nos plantões de vendas das incorporadoras. "

```html
<!DOCTYPE html>
<html lang="pt-BR">
<head>
<meta charset="UTF-8">
<title>Crachá — Valenorte Imóveis</title>
<link rel="stylesheet" href="https://fonts.googleapis.com/css2?family=Lato:wght@400;700&display=swap">
<style>
  :root {
    --backdrop: #e9e9e7;
    --badge-dark: #2d2d2d;
    --badge-light: #ffffff;
    --accent-gold: #e8b436;
    --text-dark: #1c1c1c;
    --text-muted: #2b2b2b;
  }
  * { margin: 0; padding: 0; box-sizing: border-box; }
  html, body {
    width: 1200px;
    height: 1200px;
    overflow: hidden;
    background: var(--backdrop);
    font-family: "Lato", sans-serif;
  }
  .canvas {
    position: relative;
    width: 1200px;
    height: 1200px;
  }
  .id-badge {
    position: absolute;
    left: 360px;
    top: 221px;
    width: 480px;
    height: 763px;
    background: var(--badge-light);
    overflow: hidden;
    box-shadow: 0 2px 10px rgba(0,0,0,0.12);
  }
  .badge-header {
    position: absolute;
    left: 0; top: 0;
    width: 100%;
    height: 422px;
    background: var(--badge-dark);
  }
  .brand {
    position: absolute;
    top: 106px;
    left: 0;
    width: 100%;
    display: flex;
    align-items: center;
    justify-content: center;
    gap: 16px;
  }
  .brand-square {
    width: 44px;
    height: 44px;
    background: var(--accent-gold);
  }
  .brand-name {
    color: var(--badge-light);
    font-weight: 400;
    font-size: 36px;
    letter-spacing: 2px;
    line-height: 1;
  }
  .photo-slot {
    position: absolute;
    left: 96px;
    top: 259px;
    width: 288px;
    height: 288px;
    border-radius: 50%;
    background: var(--badge-light);
    border: 7px solid var(--accent-gold);
  }
  .holder-name {
    position: absolute;
    top: 600px;
    left: 0;
    width: 100%;
    text-align: center;
    font-size: 43px;
    font-weight: 400;
    color: var(--text-dark);
  }
  .holder-role {
    position: absolute;
    top: 655px;
    left: 0;
    width: 100%;
    text-align: center;
    font-size: 25px;
    letter-spacing: 3px;
    color: var(--text-muted);
  }
  .accent-bar {
    position: absolute;
    left: 43px;
    bottom: 0;
    width: 394px;
    height: 24px;
    background: var(--accent-gold);
    border-radius: 12px 12px 0 0;
  }
</style>
</head>
<body>
  <div class="canvas">
    <div class="id-badge">
      <div class="badge-header">
        <div class="brand">
          <span class="brand-square"></span>
          <span class="brand-name">VALENORTE IMÓVEIS</span>
        </div>
      </div>
      <div class="photo-slot" role="img" aria-label="Espaço para a foto do corretor"></div>
      <p class="holder-name">Nome Sobrenome</p>
      <p class="holder-role">CARGO / FUNÇÃO</p>
      <div class="accent-bar"></div>
    </div>
  </div>
</body>
</html>
```